Business Card Design

I'm a commercial general contractor remodel offices, hotels, health clubs and stores mostly San Francisco and the peninsula
the file I down loaded is kind of what I want I like the I beam with my company name in it, that would be fine with me but if you have better Idea will look at it you never know, I'm decided to give in and change my company name to how every one knows me, I have been in business since 1991, I like the I beam logo I included one of my old card from my old company for reference for you.

Industry/Entity Type

Business

Contact Information for Business Card

BRAXO CONSTRUCTION (is my company name)
Wendell Trusk contractor, LIc 314827
4158 Garnet Row, San Bruno, California 94066
mobile, (415) 555-0147
phone (650) 555-0182
Fax, (650) 555-0183
email, braxo@braxoconstruction.example

```html
<!DOCTYPE html>
<html lang="en">
<head>
<meta charset="utf-8">
<title>Braxo Construction – Business Card</title>
<link href="https://fonts.googleapis.com/css2?family=Open+Sans:wght@400;700&display=swap" rel="stylesheet">
<style>
  :root {
    --backdrop: #2b2b2b;
    --card: #161616;
    --card-edge: #1f1f1f;
    --text-light: #f2f2f2;
    --accent-blue: #1f7fd6;
  }
  html, body {
    margin: 0;
    padding: 0;
    width: 1200px;
    height: 900px;
    overflow: hidden;
    background: var(--backdrop);
    font-family: "Open Sans", Arial, sans-serif;
  }
  .canvas {
    position: relative;
    width: 1200px;
    height: 900px;
  }
  .card {
    position: absolute;
    top: 300px;
    width: 525px;
    height: 300px;
    background: var(--card);
    border: 1px solid var(--card-edge);
    border-radius: 26px;
    box-sizing: border-box;
  }
  .card--contact { left: 50px; }
  .card--brand { left: 625px; }

  .brand-mark {
    position: absolute;
    display: flex;
    align-items: center;
    gap: 8px;
    color: var(--accent-blue);
    font-weight: 700;
    letter-spacing: 0.5px;
    white-space: nowrap;
  }
  .brand-mark__square {
    width: 14px;
    height: 14px;
    background: var(--accent-blue);
  }
  .card--contact .brand-mark {
    left: 28px;
    top: 138px;
    font-size: 17px;
  }
  .card--brand .brand-mark {
    left: 50%;
    top: 50%;
    transform: translate(-50%, -50%);
    font-size: 26px;
    gap: 12px;
  }
  .card--brand .brand-mark__square {
    width: 20px;
    height: 20px;
  }

  .contact {
    position: absolute;
    left: 272px;
    top: 40px;
    color: var(--text-light);
    font-size: 14px;
    line-height: 1.35;
  }
  .contact__name {
    font-size: 20px;
    margin: 0 0 2px;
    font-weight: 400;
  }
  .contact__role { color: var(--accent-blue); }
  .contact__licence { margin-bottom: 10px; }
  .contact__address { margin-bottom: 10px; }
  .contact__line { margin: 2px 0; }
  .contact__label { color: var(--accent-blue); }
</style>
</head>
<body>
  <main class="canvas">
    <section class="card card--contact">
      <div class="brand-mark">
        <span class="brand-mark__square"></span>
        <span class="brand-mark__name">BRAXO CONSTRUCTION</span>
      </div>
      <div class="contact">
        <h1 class="contact__name">Wendell Trusk</h1>
        <div class="contact__role">Contractor,</div>
        <div class="contact__licence">LIc 314827</div>
        <div class="contact__address">4158 Garnet Row, San Bruno,<br>California 94066</div>
        <div class="contact__line"><span class="contact__label">M:</span> (415) 555-0147</div>
        <div class="contact__line"><span class="contact__label">T:</span>(650) 555-0182</div>
        <div class="contact__line"><span class="contact__label">F:</span>(650) 555-0183</div>
        <div class="contact__line"><span class="contact__label">E:</span>braxo@braxoconstruction.example</div>
      </div>
    </section>

    <section class="card card--brand">
      <div class="brand-mark">
        <span class="brand-mark__square"></span>
        <span class="brand-mark__name">BRAXO CONSTRUCTION</span>
      </div>
    </section>
  </main>
</body>
</html>
```